FotoVELTA buisnesscard

Hey :) I need a modern buisnesscard for my company FotoVELTA
It most have:
Dagligleder og Fotograf: Henrik Torvald Bjelland

Mob: +4791642058
Epost: post@fotovelta.no
Adresse: Bakkestien22, 7010 Trondheim

Facbook and instagram logo with text FotoVELTA

FotoVELTA logo

It Company

```html
<!DOCTYPE html>
<html lang="no">
<head>
<meta charset="utf-8">
<title>FotoVELTA – visittkort</title>
<link href="https://fonts.googleapis.com/css2?family=Catamaran:wght@600;700;800&display=swap" rel="stylesheet">
<style>
  :root {
    --card-dark: #5e5a59;
    --card-light: #9b9b9b;
    --text-light: #ffffff;
    --social-grey: #e6e6e6;
    --brand-pink: #e8298f;
    --brand-blue: #00aeef;
    --page: #ffffff;
  }
  * { margin: 0; padding: 0; box-sizing: border-box; }
  html, body {
    width: 1016px; height: 1200px; overflow: hidden;
    background: var(--page);
    font-family: "Catamaran", sans-serif;
  }
  .sheet { position: relative; width: 1016px; height: 1200px; }
  .card {
    position: absolute; left: 2px; width: 1013px; height: 579px;
    border-radius: 33px;
    background: linear-gradient(28deg, var(--card-dark) 0%, #7d7a79 50%, var(--card-light) 100%);
    overflow: hidden;
  }
  .card--front { top: 0; }
  .card--back { top: 620px; }

  .wordmark { position: absolute; font-weight: 800; color: var(--brand-pink); line-height: 1; letter-spacing: -1px; white-space: nowrap; }
  .card--front .wordmark { right: 30px; top: 162px; font-size: 60px; }
  .card--front .wordmark-square { position: absolute; right: 126px; top: 39px; width: 120px; height: 120px; background: var(--brand-blue); }

  .holder-name {
    position: absolute; left: 84px; top: 212px;
    font-size: 40px; font-weight: 600; letter-spacing: 0.5px;
    color: var(--text-light); line-height: 1; white-space: nowrap;
  }
  .holder-role {
    position: absolute; left: 146px; top: 280px;
    font-size: 28px; font-weight: 600; color: var(--text-light); line-height: 1;
  }
  .contact-row { position: absolute; left: 92px; display: flex; align-items: center; }
  .contact-row svg { width: 48px; flex: none; }
  .contact-row span {
    margin-left: 17px; font-size: 38px; font-weight: 700;
    color: var(--text-light); line-height: 1; white-space: nowrap;
  }
  .row-phone { top: 346px; }
  .row-phone svg { height: 72px; }
  .row-mail { top: 430px; }
  .row-mail svg { height: 44px; }
  .row-address { top: 494px; }
  .row-address svg { height: 48px; }

  .card--back .wordmark-square {
    position: absolute; left: 406px; top: 102px; width: 200px; height: 200px;
    background: var(--brand-blue);
  }
  .card--back .wordmark {
    left: 0; right: 0; text-align: center; top: 312px; font-size: 100px;
  }
  .social { position: absolute; top: 484px; display: flex; align-items: center; gap: 12px; }
  .social-left { left: 63px; }
  .social-right { right: 78px; }
  .social-badge { width: 57px; height: 57px; border-radius: 8px; background: var(--social-grey); }
  .social-name { font-size: 24px; font-weight: 700; color: var(--social-grey); line-height: 1; padding-top: 4px; }
</style>
</head>
<body>
<div class="sheet">

  <section class="card card--front">
    <div class="wordmark-square"></div>
    <div class="wordmark">FotoVELTA</div>

    <h1 class="holder-name">HENRIK TORVALD BJELLAND</h1>
    <p class="holder-role">Dagligleder og Fotograf</p>

    <div class="contact">
      <div class="contact-row row-phone">
        <svg viewBox="0 0 48 72" aria-hidden="true">
          <rect x="8" y="2" width="32" height="68" rx="4" fill="none" stroke="#fff" stroke-width="3"/>
          <line x1="8" y1="10" x2="40" y2="10" stroke="#fff" stroke-width="2"/>
          <line x1="8" y1="60" x2="40" y2="60" stroke="#fff" stroke-width="2"/>
          <line x1="20" y1="6" x2="28" y2="6" stroke="#fff" stroke-width="1.5"/>
          <circle cx="24" cy="65" r="2" fill="#fff"/>
        </svg>
        <span>+479 164 2058</span>
      </div>
      <div class="contact-row row-mail">
        <svg viewBox="0 0 48 36" aria-hidden="true">
          <rect x="1.5" y="1.5" width="45" height="33" fill="none" stroke="#fff" stroke-width="3"/>
          <polyline points="2,3 24,22 46,3" fill="none" stroke="#fff" stroke-width="3"/>
          <line x1="2" y1="33" x2="18" y2="17" stroke="#fff" stroke-width="3"/>
          <line x1="46" y1="33" x2="30" y2="17" stroke="#fff" stroke-width="3"/>
        </svg>
        <span>post@fotovelta.no</span>
      </div>
      <div class="contact-row row-address">
        <svg viewBox="0 0 48 48" aria-hidden="true">
          <path d="M24 46 C14 34 6 27 6 18 A18 18 0 0 1 42 18 C42 27 34 34 24 46 Z" fill="none" stroke="#fff" stroke-width="3"/>
          <circle cx="24" cy="18" r="7" fill="none" stroke="#fff" stroke-width="3"/>
        </svg>
        <span>Bakkestien22, 7010 Trondheim</span>
      </div>
    </div>
  </section>

  <section class="card card--back">
    <div class="wordmark-square"></div>
    <div class="wordmark">FotoVELTA</div>

    <div class="social social-left">
      <div class="social-badge"></div>
      <span class="social-name">FotoVELTA</span>
    </div>
    <div class="social social-right">
      <span class="social-name">FotoVELTA</span>
      <div class="social-badge"></div>
    </div>
  </section>

</div>
</body>
</html>
```